Need to make a work slip for trucking company.

I need a form to fill out for my truck drivers to get signed on delivery. It is for a trucking company and this form will be for each machine equipment move. I have included my old sheet which I need Updated. Its going on a 9.5 inch by 8.5 inch sheet of paper. It should have room for the day, date, customer name, ordered by, P.O. Number, Project Number, Driver, Truck/Trailer, Tolls (needs more room then my old sheet need a few lines under each other for each toll during the machine move), Permits, some room for other information, Loads, Hours, and 2 lines for a Signature and Print Line.
Updates

Need to also include a Pickup Address and a Deliver Address with lines to write in. Also I need to add a Print Line (and labeled Print) for whoever is signing the ticket.

Requirements
Must have
• My new company name and Logo. I have included my new Logo. It must be easy to ready. Must include my company colors. (Concrete Gray, and Neon Blue)

```html
<!DOCTYPE html>
<html lang="en">
<head>
<meta charset="UTF-8">
<title>Northridge Hauling – Equipment Move Work Slip</title>
<link href="https://fonts.googleapis.com/css2?family=Poppins:wght@400;700&display=swap" rel="stylesheet">
<style>
  :root {
    --brand-blue: #176cb5;
    --paper: #ffffff;
    --backdrop: #f1f5fa;
    --ink: #454545;
    --rule: #a3a3a3;
  }
  * { margin: 0; padding: 0; box-sizing: border-box; }
  html, body { width: 904px; height: 1200px; overflow: hidden; }
  body { position: relative; background: var(--backdrop); font-family: "Poppins", sans-serif; color: var(--ink); }
  .backdrop { position: absolute; inset: 0; }
  .header-band { position: absolute; left: 0; top: 0; width: 904px; height: 276px; background: var(--brand-blue); }
  .brand-name {
    position: absolute; left: 0; top: 50px; width: 904px; text-align: center;
    font-weight: 700; font-size: 34px; letter-spacing: 2px; color: var(--paper); line-height: 40px;
  }
  .slip { position: absolute; left: 52px; top: 142px; width: 801px; height: 995px; background: var(--paper); }
  .day {
    position: absolute; top: 36px; width: 51px; height: 24px; background: var(--brand-blue);
    color: var(--paper); font-family: Arial, Helvetica, sans-serif; font-size: 10.5px;
    line-height: 24px; text-align: center;
  }
  .field-label {
    position: absolute; font-size: 13.5px; line-height: 20px; white-space: nowrap; color: var(--ink);
  }
  .date-label { font-family: Arial, Helvetica, sans-serif; font-size: 10.5px; }
  .write-line { position: absolute; height: 0; border-top: 1px solid var(--rule); }
  .roll-option { position: absolute; font-size: 13.5px; line-height: 20px; display: flex; align-items: center; gap: 5px; }
  .radio { width: 13px; height: 13px; border: 1px solid #6f6f6f; border-radius: 50%; display: inline-block; }
  .footer-note {
    position: absolute; left: 0; top: 1157px; width: 904px; text-align: center;
    font-family: Arial, Helvetica, sans-serif; font-size: 10px; color: var(--paper);
  }
  .form-code { position: absolute; left: 863px; top: 1155px; font-size: 13px; color: var(--paper); }
</style>
</head>
<body>
  <svg class="backdrop" width="904" height="1200" viewBox="0 0 904 1200" aria-hidden="true">
    <polygon points="0,1200 904,748 904,1200" fill="#176cb5"/>
  </svg>
  <div class="header-band"></div>
  <div class="brand-name">NORTHRIDGE HAULING</div>

  <main class="slip">
    <div class="day" style="left:25px">MON</div>
    <div class="day" style="left:82px">TUE</div>
    <div class="day" style="left:140px">WED</div>
    <div class="day" style="left:197px">THR</div>
    <div class="day" style="left:255px">FRI</div>
    <div class="day" style="left:312px">SAT</div>
    <div class="day" style="left:370px">SUN</div>

    <div class="field-label date-label" style="left:653px;top:38px">DATE</div>
    <div class="write-line" style="left:681px;top:53px;width:95px"></div>

    <div class="field-label" style="left:25px;top:118px">Customer Name</div>
    <div class="write-line" style="left:150px;top:133px;width:511px"></div>

    <div class="field-label" style="left:25px;top:169px">Ordered by</div>
    <div class="write-line" style="left:106px;top:184px;width:556px"></div>

    <div class="field-label" style="left:25px;top:221px">P.O. Number</div>
    <div class="write-line" style="left:115px;top:236px;width:241px"></div>
    <div class="field-label" style="left:370px;top:221px">Project Number</div>
    <div class="write-line" style="left:477px;top:236px;width:186px"></div>

    <div class="field-label" style="left:25px;top:270px">Roll :</div>
    <div class="roll-option" style="left:73px;top:270px"><span class="radio"></span>F/B</div>
    <div class="roll-option" style="left:145px;top:270px"><span class="radio"></span>L/B</div>
    <div class="roll-option" style="left:210px;top:270px"><span class="radio"></span>LD</div>
    <div class="roll-option" style="left:266px;top:270px"><span class="radio"></span>STR/TRL</div>
    <div class="roll-option" style="left:363px;top:270px"><span class="radio"></span>BM/Tk</div>
    <div class="roll-option" style="left:450px;top:270px"><span class="radio"></span>Dump Tk</div>

    <div class="field-label" style="left:25px;top:314px">Driver</div>
    <div class="write-line" style="left:71px;top:329px;width:257px"></div>

    <div class="field-label" style="left:25px;top:357px">Truck/Trailer</div>
    <div class="write-line" style="left:120px;top:372px;width:211px"></div>

    <div class="field-label" style="left:25px;top:399px">Equipment Types</div>
    <div class="write-line" style="left:147px;top:414px;width:183px"></div>

    <div class="field-label" style="left:25px;top:444px">Tolls</div>
    <div class="write-line" style="left:65px;top:459px;width:598px"></div>
    <div class="write-line" style="left:65px;top:503px;width:598px"></div>
    <div class="write-line" style="left:65px;top:549px;width:598px"></div>

    <div class="field-label" style="left:25px;top:581px">Permits</div>
    <div class="write-line" style="left:88px;top:594px;width:575px"></div>

    <div class="field-label" style="left:25px;top:629px">Equipment Type</div>
    <div class="write-line" style="left:145px;top:644px;width:518px"></div>

    <div class="field-label" style="left:25px;top:679px">Pickup Address</div>
    <div class="write-line" style="left:136px;top:694px;width:527px"></div>

    <div class="field-label" style="left:25px;top:729px">Delivery Address</div>
    <div class="write-line" style="left:145px;top:744px;width:518px"></div>

    <div class="field-label" style="left:25px;top:780px">Loads</div>
    <div class="write-line" style="left:71px;top:795px;width:192px"></div>
    <div class="field-label" style="left:281px;top:780px">Hours</div>
    <div class="write-line" style="left:328px;top:795px;width:200px"></div>

    <div class="field-label" style="left:25px;top:835px">Signature</div>
    <div class="write-line" style="left:113px;top:850px;width:550px"></div>

    <div class="field-label" style="left:25px;top:882px">Print</div>
    <div class="write-line" style="left:62px;top:897px;width:601px"></div>
  </main>

  <div class="footer-note">© COPYRIGHT 2020 NORTHRIDGE HAULING. ALL RIGHTS RESERVED.</div>
  <div class="form-code">C2</div>
</body>
</html>
```